Redesign of 3-4 page site for professional services firm

Our site is www.kestrelvaleadvisors.com. We currently have a simple page made with HostPlumo tools. But the tools are not able to generate the look and feel we desire. We need a home page similar to current that tells a little about our company, our experience and our team. We need a second page to show details of current and past transactions we have assisted our clients with. Currently this page reads like a word document but we would like for it to present in a cleaner fashion and liven it up with some images that link to the industry served. For example, a motorcycle outline in a circle for the powersports related transactions. We would like page to introduce each member of "Our Team" and highlight their experience with a photo of each person. If there is no photo available, we would like a placeholder to be their initials in a circle that can be updated later. We would also like a contact us section whether this is a different page or part of the home page.

Target Market(s)

Retirement minded business owners

Industry/Entity Type

Professional Services

Coding

Coded - Design and coding required

Requirements
Must have
• See project description. Must include a page or section for "Current Listings" and "Recently Completed Transactions" (can be same page)

```html
<!DOCTYPE html>
<html lang="en">
<head>
<meta charset="utf-8">
<title>Kestrel Vale Advisors</title>
<link href="https://fonts.googleapis.com/css2?family=Poppins:ital,wght@0,400;0,500;0,600;0,700;1,400&family=Outfit:wght@500;700&display=swap" rel="stylesheet">
<style>
:root{
  --red:#d0111b;
  --green:#1fb800;
  --green-soft:#ebfbe8;
  --ink:#111111;
  --text:#333333;
  --muted:#666666;
  --card:#f2f2f2;
  --line:#d6d6d6;
  --dark:#0b0b0b;
  --darker:#161616;
}
*{box-sizing:border-box;margin:0;padding:0}
html,body{width:1200px;height:5085px;overflow:hidden;background:#fff}
body{position:relative;font-family:"Poppins",sans-serif;color:var(--text)}
.abs{position:absolute}
.heading{font-family:"Outfit",sans-serif;font-weight:700;color:var(--ink);font-size:58px;line-height:1;letter-spacing:.5px}
.eyebrow{font-family:"Poppins",sans-serif;color:var(--red);font-size:24px;line-height:1;display:flex;align-items:center;gap:8px}
.eyebrow.center{justify-content:center;left:0;right:0}
.eyebrow .dash{display:inline-block;width:34px;height:2px;background:var(--red)}
.center-text{left:0;right:0;text-align:center}

/* header */
.brand{left:68px;top:28px;font-size:34px;font-weight:600;color:var(--ink);display:flex;align-items:center;gap:12px}
.brand .mark{width:18px;height:18px;border-radius:50%;background:var(--red)}
.top-phone{left:790px;top:30px;width:170px;height:36px;background:var(--ink);color:#fff;font-size:14px;display:flex;align-items:center;justify-content:center;gap:8px;clip-path:polygon(8% 0,100% 0,100% 100%,0 100%)}
.top-cta{left:958px;top:30px;width:182px;height:36px;background:var(--green);color:#fff;font-size:13px;font-weight:500;display:flex;align-items:center;justify-content:center;clip-path:polygon(8% 0,100% 0,92% 100%,0 100%)}
.nav{left:456px;top:80px;display:flex;gap:36px;font-size:13px;color:var(--ink)}
.nav a{color:inherit;text-decoration:none;padding-bottom:6px}
.nav a.active{color:var(--red);border-bottom:2px solid var(--red)}

/* hero */
.hero{left:0;top:123px;width:1200px;height:777px;background:linear-gradient(100deg,#4a4038 0%,#2b2520 45%,#141414 100%);clip-path:polygon(0 0,100% 0,100% 92%,0 100%)}
.hero-copy{left:618px;top:262px;width:540px;color:#fff}
.hero-copy .kicker{color:var(--green);font-size:25px;font-weight:500}
.hero-copy h1{font-family:"Poppins",sans-serif;font-weight:600;font-size:46px;line-height:58px;margin-top:8px}
.hero-copy p{font-size:20px;line-height:44px;margin-top:18px}
.btn-red{display:inline-flex;align-items:center;justify-content:center;width:305px;height:74px;margin-top:36px;background:var(--red);color:#fff;font-weight:600;font-size:22px;clip-path:polygon(8% 0,100% 0,92% 100%,0 100%)}
.dots{left:552px;top:792px;display:flex;gap:12px;align-items:center}
.dots i{display:block;width:11px;height:11px;border-radius:50%;background:#fff}
.dots i.on{width:26px;height:6px;border-radius:3px;background:var(--green)}

/* about */
.about-copy{left:155px;top:1018px;width:335px}
.about-copy .heading{margin-top:18px}
.about-copy p{font-size:13px;line-height:28px;margin-top:28px;text-align:justify;color:var(--text)}
.btn-green{display:flex;align-items:center;justify-content:center;background:var(--green);color:#fff;font-weight:600;font-size:15px;clip-path:polygon(8% 0,100% 0,92% 100%,0 100%)}
.about-btn{left:155px;top:1384px;width:168px;height:42px}
.slant-frame{border:2px solid var(--green);clip-path:none}
.about-frame{left:560px;top:978px;width:485px;height:478px}
.about-photo{left:538px;top:988px;width:493px;height:478px;background:linear-gradient(135deg,#dfe6ec,#8aa4bb 55%,#3f5870);clip-path:polygon(16% 0,100% 0,84% 100%,0 100%)}

/* team */
.team-intro{top:1690px;left:130px;width:940px;text-align:center;font-size:13px;line-height:28px;color:var(--text)}
.member{top:1873px;width:330px;height:410px;border-radius:30px;background:var(--card);border:1px solid var(--line)}
.member.featured{background:var(--green-soft);border-color:var(--green)}
.member .portrait{position:absolute;left:55px;top:-56px;width:220px;height:220px;border-radius:50%;border:6px solid #fff;background:radial-gradient(circle at 50% 40%,#d9c3b1,#8b7a6e 60%,#3a3a3a);box-shadow:0 4px 12px rgba(0,0,0,.12)}
.member h3{position:absolute;top:205px;left:0;right:0;text-align:center;font-size:21px;font-weight:600;color:var(--red)}
.member.featured h3{color:var(--green)}
.member p{position:absolute;top:245px;left:0;right:0;text-align:center;font-size:20px;color:var(--text)}
.member .social{position:absolute;left:134px;top:305px;width:62px;height:62px;border-radius:50%;background:var(--red)}
.member.featured .social{background:var(--green)}
.arrows{display:flex;gap:12px;left:0;right:0;justify-content:center}
.arrows span{width:54px;height:54px;border-radius:50%;display:flex;align-items:center;justify-content:center;background:#fff;box-shadow:0 2px 8px rgba(0,0,0,.15)}
.arrows span.next{background:var(--ink)}

/* listings */
.listing-photo{top:2668px;height:477px}
.listing-left{left:68px;width:537px;background:linear-gradient(135deg,#e6e2dc,#9c9185 50%,#2f2f2f);clip-path:polygon(7% 0,100% 0,93% 100%,0 100%)}
.listing-right{left:567px;width:540px;background:linear-gradient(135deg,#f4f4f4,#c9ccd0 50%,#6a6e74);clip-path:polygon(7% 0,100% 0,93% 100%,0 100%)}
.listing-cap{top:3174px;font-size:26px;font-weight:500;color:var(--ink)}

/* testimonials */
.review{top:3478px;width:345px;height:150px;background:#fff;box-shadow:0 4px 16px rgba(0,0,0,.1);padding:32px 28px 0}
.review p{font-size:13px;font-style:italic;line-height:25px;text-align:justify;text-align-last:center;color:var(--text)}
.review .quote{position:absolute;left:26px;top:-16px}
.author{top:3662px;display:flex;gap:16px;align-items:center}
.author .avatar{width:58px;height:58px;border-radius:50%;background:radial-gradient(circle,#cdb9a6,#6c625a);border:3px solid #eee}
.author b{display:block;color:var(--red);font-size:18px;font-weight:600;line-height:22px}
.author small{display:block;font-size:12px;color:var(--muted)}
.author .stars{color:#f4b400;font-size:11px;letter-spacing:1px}

/* contact */
.contact-frame{left:108px;top:3985px;width:500px;height:490px}
.contact-photo{left:118px;top:3995px;width:494px;height:472px;background:linear-gradient(135deg,#6b4a33,#a87a55 45%,#3a2a1f);clip-path:polygon(10% 0,100% 0,90% 100%,0 100%)}
.contact-head{left:677px;top:4018px}
.field{background:#fff;border:1px solid #e3e3e3;box-shadow:0 2px 6px rgba(0,0,0,.06);font-size:11px;color:#9a9a9a;padding:10px 18px}
.submit{left:677px;top:4413px;width:168px;height:44px;font-size:18px}

/* footer */
.footer{left:0;top:4660px;width:1200px;height:425px;background:var(--dark);clip-path:polygon(0 5%,100% 0,100% 100%,0 100%)}
.footer-bar{left:0;top:5010px;width:1200px;height:75px;background:var(--darker)}
.foot-brand{left:68px;top:4840px;font-size:48px;font-weight:600;color:#fff;display:flex;align-items:center;gap:14px}
.foot-brand .mark{width:26px;height:26px;border-radius:50%;background:var(--red)}
.foot-col h4{font-size:20px;font-weight:500;color:#fff;margin-bottom:22px}
.foot-col ul{list-style:none}
.foot-col li{font-size:13px;color:#fff;line-height:26px;display:flex;align-items:center;gap:12px}
.foot-col li::before{content:"";width:7px;height:7px;border-radius:50%;background:var(--red)}
.contact-list li::before{display:none}
.contact-list li{align-items:flex-start;line-height:17px;margin-bottom:18px}
.contact-list .ic{flex:none;width:24px;height:24px;border-radius:4px;background:var(--green);display:flex;align-items:center;justify-content:center}
.news p{font-size:13px;color:#fff;line-height:17px;width:200px}
.news .input{margin-top:20px;width:195px;height:32px;background:#fff}
.news .go{margin-top:18px;width:100px;height:32px;font-size:10px}
.copy{left:68px;top:5040px;font-size:12px;color:#ddd}
.socials{left:1015px;top:5034px;display:flex;gap:7px}
.socials i{display:block;width:24px;height:24px;border-radius:50%;background:var(--red)}
</style>
</head>
<body>

<!-- Header -->
<div class="abs brand"><span class="mark"></span>Kestrel Vale</div>
<div class="abs top-phone">
  <svg width="16" height="16" viewBox="0 0 24 24" fill="#fff"><path d="M6.6 10.8a15 15 0 0 0 6.6 6.6l2.2-2.2c.3-.3.7-.4 1-.2 1.1.4 2.3.6 3.6.6.6 0 1 .4 1 1V20c0 .6-.4 1-1 1A17 17 0 0 1 3 4c0-.6.4-1 1-1h3.5c.6 0 1 .4 1 1 0 1.3.2 2.5.6 3.6.1.3 0 .7-.2 1z"/></svg>
  555-014-2290
</div>
<div class="abs top-cta">GET STARTED TODAY</div>
<nav class="abs nav">
  <a class="active">HOME</a><a>ABOUT US</a><a>OUR EXPERIENCE</a><a>OUR TEAM</a><a>BUSINESS LISTINGS</a><a>CONTACT US</a>
</nav>

<!-- Hero -->
<div class="abs hero" role="img" aria-label="Overhead photo of business team joining hands across a meeting table"></div>
<div class="abs hero-copy">
  <div class="kicker">WELCOME TO KESTREL VALE</div>
  <h1>Strategically Navigating Business Exits</h1>
  <p>Lorem ipsum dolor sit amet, consectetur adipiscing elit, sed do eiusmod tempor incididunt ut labore et dolore magna aliqua Ut enim ad minim.</p>
  <div class="btn-red">GET STARTED TODAY</div>
</div>
<div class="abs dots"><i class="on"></i><i></i><i></i><i></i></div>

<!-- About -->
<section class="abs about-copy">
  <div class="eyebrow">Who We Are <span class="dash"></span></div>
  <h2 class="heading">ABOUT US</h2>
  <p>At Kestrel Vale Advisors, our mission is to empower entrepreneurs and business owners by facilitating seamless transactions that lead to mutual success. We understand that selling or acquiring a business can be a complex and emotional journey, which is why our dedicated team of experts is here to guide you every step of the way.</p>
</section>
<div class="abs btn-green about-btn">READ MORE</div>
<svg class="abs" style="left:538px;top:978px" width="510" height="490"><polygon points="50,2 508,2 460,488 2,488" fill="none" stroke="#1fb800" stroke-width="2"/></svg>
<div class="abs about-photo" role="img" aria-label="Photo of hands using a tablet showing business charts"></div>

<!-- Team -->
<div class="abs eyebrow center" style="top:1578px"><span class="dash"></span>Meet Our Team<span class="dash"></span></div>
<h2 class="abs heading center-text" style="top:1612px">OUR TEAM</h2>
<p class="abs team-intro">Together, our team of CPAs, attorneys, real estate brokers, and financial advisors work collaboratively to provide you with a holistic approach to business transactions. With our combined knowledge and experience, we strive to ensure a smooth and successful journey for our clients, delivering exceptional results and peace of mind.</p>

<div class="abs member" style="left:70px">
  <div class="portrait" role="img" aria-label="Portrait photo of team member"></div>
  <h3>WARRENASHBY</h3><p>Lorem ipsum</p><span class="social"></span>
</div>
<div class="abs member featured" style="left:440px">
  <div class="portrait" role="img" aria-label="Portrait photo of team member"></div>
  <h3>COLINTREADWAY</h3><p>Lorem ipsum</p><span class="social"></span>
</div>
<div class="abs member" style="left:806px">
  <div class="portrait" role="img" aria-label="Portrait photo of team member"></div>
  <h3>MARTINELLERY</h3><p>Lorem ipsum</p><span class="social"></span>
</div>
<div class="abs arrows" style="top:2344px">
  <span><svg width="20" height="14" viewBox="0 0 20 14"><path d="M19 7H2M7 1 1 7l6 6" stroke="#111" stroke-width="2.4" fill="none"/></svg></span>
  <span class="next"><svg width="20" height="14" viewBox="0 0 20 14"><path d="M1 7h17M13 1l6 6-6 6" stroke="#fff" stroke-width="2.4" fill="none"/></svg></span>
</div>

<!-- Listings -->
<div class="abs eyebrow center" style="top:2508px"><span class="dash"></span>Listings<span class="dash"></span></div>
<h2 class="abs heading center-text" style="top:2542px">BUSINESS LISTINGS</h2>
<div class="abs listing-photo listing-left" role="img" aria-label="Photo of professionals working at a laptop in an office"></div>
<div class="abs listing-photo listing-right" role="img" aria-label="Photo of a handshake over a signed contract"></div>
<div class="abs listing-cap" style="left:133px">Current Business Listings</div>
<div class="abs listing-cap" style="left:564px">Recently Completed Business Sales</div>

<!-- Testimonials -->
<div class="abs eyebrow center" style="top:3325px"><span class="dash"></span>Reviews<span class="dash"></span></div>
<h2 class="abs heading center-text" style="top:3358px">OUR TESTIMONIALS</h2>

<div class="abs review" style="left:68px">
  <svg class="quote" width="52" height="40" viewBox="0 0 52 40"><path d="M2 40V22C2 10 8 3 20 0l2 5c-6 2-9 6-9 12h9v23zM30 40V22C30 10 36 3 48 0l2 5c-6 2-9 6-9 12h9v23z" fill="#1fb800"/></svg>
  <p>Lorem ipsum dolor sit amet, conse ctetuer adipiscing elit. Aenean comodo ligula eget dolor. Aenean massa. Cum sociis natoque pen atibus et magnis</p>
</div>
<div class="abs review" style="left:428px">
  <svg class="quote" width="52" height="40" viewBox="0 0 52 40"><path d="M2 40V22C2 10 8 3 20 0l2 5c-6 2-9 6-9 12h9v23zM30 40V22C30 10 36 3 48 0l2 5c-6 2-9 6-9 12h9v23z" fill="#1fb800"/></svg>
  <p>Lorem ipsum dolor sit amet, conse ctetuer adipiscing elit. Aenean comodo ligula eget dolor. Aenean massa. Cum sociis natoque pen atibus et magnis</p>
</div>
<div class="abs review" style="left:790px">
  <svg class="quote" width="52" height="40" viewBox="0 0 52 40"><path d="M2 40V22C2 10 8 3 20 0l2 5c-6 2-9 6-9 12h9v23zM30 40V22C30 10 36 3 48 0l2 5c-6 2-9 6-9 12h9v23z" fill="#1fb800"/></svg>
  <p>Lorem ipsum dolor sit amet, conse ctetuer adipiscing elit. Aenean comodo ligula eget dolor. Aenean massa. Cum sociis natoque pen atibus et magnis</p>
</div>
<div class="abs author" style="left:134px"><span class="avatar" role="img" aria-label="Reviewer photo"></span><div><b>Daniel Whitcombe</b><small>Managing Director</small><span class="stars">★★★★★</span></div></div>
<div class="abs author" style="left:495px"><span class="avatar" role="img" aria-label="Reviewer photo"></span><div><b>Owen Marsh</b><small>Managing Director</small><span class="stars">★★★★★</span></div></div>
<div class="abs author" style="left:856px"><span class="avatar" role="img" aria-label="Reviewer photo"></span><div><b>Peter Langley</b><small>Managing Director</small><span class="stars">★★★★★</span></div></div>
<div class="abs arrows" style="top:3796px">
  <span><svg width="20" height="14" viewBox="0 0 20 14"><path d="M19 7H2M7 1 1 7l6 6" stroke="#111" stroke-width="2.4" fill="none"/></svg></span>
  <span class="next"><svg width="20" height="14" viewBox="0 0 20 14"><path d="M1 7h17M13 1l6 6-6 6" stroke="#fff" stroke-width="2.4" fill="none"/></svg></span>
</div>

<!-- Contact -->
<svg class="abs" style="left:106px;top:3983px" width="510" height="496"><polygon points="60,2 508,2 450,494 2,494" fill="none" stroke="#1fb800" stroke-width="2"/></svg>
<div class="abs contact-photo" role="img" aria-label="Photo of smiling colleagues shaking hands in a meeting"></div>
<div class="abs contact-head">
  <div class="eyebrow">Get In Touch <span class="dash"></span></div>
  <h2 class="heading" style="margin-top:18px">CONTACT US</h2>
</div>
<div class="abs field" style="left:677px;top:4147px;width:200px;height:40px">First Name:</div>
<div class="abs field" style="left:895px;top:4147px;width:198px;height:40px">Last Name:</div>
<div class="abs field" style="left:677px;top:4205px;width:200px;height:40px">Phone:</div>
<div class="abs field" style="left:895px;top:4205px;width:198px;height:40px">Email:</div>
<div class="abs field" style="left:677px;top:4265px;width:416px;height:127px">Message:</div>
<div class="abs btn-green submit">SUBMIT</div>

<!-- Footer -->
<footer>
  <div class="abs footer"></div>
  <div class="abs footer-bar"></div>
  <div class="abs foot-brand"><span class="mark"></span>Kestrel Vale</div>

  <div class="abs foot-col" style="left:440px;top:4746px">
    <h4>Quick Links</h4>
    <ul><li>About Us</li><li>Our Experience</li><li>Our Team</li><li>Business Listings</li><li>Contact Us</li></ul>
  </div>

  <div class="abs foot-col" style="left:634px;top:4746px">
    <h4>Contact Us</h4>
    <ul class="contact-list">
      <li><span class="ic"><svg width="13" height="13" viewBox="0 0 24 24" fill="#fff"><path d="M6.6 10.8a15 15 0 0 0 6.6 6.6l2.2-2.2c.3-.3.7-.4 1-.2 1.1.4 2.3.6 3.6.6.6 0 1 .4 1 1V20c0 .6-.4 1-1 1A17 17 0 0 1 3 4c0-.6.4-1 1-1h3.5c.6 0 1 .4 1 1 0 1.3.2 2.5.6 3.6.1.3 0 .7-.2 1z"/></svg></span><span style="font-size:12px">CALL US<br>555-014-2290</span></li>
      <li><span class="ic"><svg width="13" height="11" viewBox="0 0 24 18"><rect x="1" y="1" width="22" height="16" fill="#fff"/><path d="M1 1l11 9 11-9" stroke="#1fb800" stroke-width="2" fill="none"/></svg></span><span style="font-size:12px">EMAIL US<br>info@kestrelvaleadvisors.com</span></li>
      <li><span class="ic"><svg width="11" height="14" viewBox="0 0 20 26" fill="#fff"><path d="M10 0a10 10 0 0 0-10 10c0 7 10 16 10 16s10-9 10-16A10 10 0 0 0 10 0zm0 14a4 4 0 1 1 0-8 4 4 0 0 1 0 8z"/></svg></span><span style="font-size:12px">48 Harlow Creek Road, Fenmore,<br>Oklahoma 74000, United States</span></li>
    </ul>
  </div>

  <div class="abs foot-col news" style="left:940px;top:4746px">
    <h4>Our Newsletter</h4>
    <p>Subscribe our newsletter to get the latest news.</p>
    <div class="input"></div>
    <div class="btn-green go">SUBSCRIBE</div>
  </div>

  <div class="abs copy">Copyright © 2023 Kestrel Vale Advisors - All Rights Reserved.</div>
  <div class="abs socials"><i></i><i></i><i></i><i></i></div>
</footer>

</body>
</html>
```